Korvel CD Cover Design Project

I need a CD front cover(front inlay) , CD top artwork, CD back cover (back inlay)
i have provided a picture and other
Artiste Name: Korvel
Song Title: Olufunke (carry me Away)
Producer: trokay
Track-list
1. Olufunke (carry me Away)
2. Olufunke (carry me Away) acapella
3. Olufunke (carry me Away) (Instrumental)
stay connected:
chirpline.net/miloskorvel
friendspace.net/miloskorvel
www.korvel-music.com
Management contact:
USA : Marla @ +15550148832 / marla@brightwavepr.com
UK: Tamsin @ +447700900417/ +447700900283 / tamsinbookings@mailhaven.co.uk
Nigeria: Funmi @ +2348000314729 / funmi@korvel-music.com
Target Market(s)
african Music consumers globally
Industry/Entity Type
Management
Look and feel
Each slider illustrates characteristics of the customer's brand and the style your logo design should communicate.

```html
<!DOCTYPE html>
<html lang="en">
<head>
<meta charset="utf-8">
<title>Korvel – Olufunke (carry me Away) CD Label</title>
<link rel="stylesheet" href="https://fonts.googleapis.com/css2?family=UnifrakturMaguntia&family=Kaushan+Script&family=Yesteryear&display=swap">
<style>
  :root {
    --page: #ffffff;
    --ink: #111111;
    --outline: #ffffff;
    --sky-top: #d4d8d6;
    --sky-low: #b9ccd4;
    --sea-deep: #2d7d96;
    --sea-light: #6cb1c0;
    --foam: #e2e7e4;
    --sand: #cdb994;
    --sand-dark: #b79f78;
    --panel: rgba(255, 255, 255, 0.62);
    --rim: #d9dcde;
    --hub-ring: #e9ebec;
    --hub-shade: #b8bcbf;
  }
  html, body {
    margin: 0;
    width: 1200px;
    height: 960px;
    overflow: hidden;
    background: var(--page);
  }
  .canvas {
    position: relative;
    width: 1200px;
    height: 960px;
    background: var(--page);
  }
  .disc {
    position: absolute;
    left: 185px;
    top: 48px;
    width: 856px;
    height: 856px;
    border-radius: 50%;
    overflow: hidden;
    box-shadow: 0 0 0 3px var(--rim), 0 4px 14px rgba(0, 0, 0, 0.28);
  }
  .disc-artwork {
    position: absolute;
    inset: 0;
    background:
      radial-gradient(ellipse 34% 46% at 64% 42%, rgba(60, 60, 60, 0.45), rgba(60, 60, 60, 0) 70%),
      linear-gradient(180deg,
        var(--sky-top) 0%,
        var(--sky-low) 21%,
        var(--sea-deep) 23%,
        var(--sea-light) 34%,
        var(--foam) 52%,
        var(--foam) 60%,
        var(--sand) 66%,
        var(--sand-dark) 100%);
  }
  .artist-name {
    position: absolute;
    left: 0;
    right: 0;
    top: 56px;
    margin: 0;
    text-align: center;
    font-family: "UnifrakturMaguntia", serif;
    font-size: 86px;
    font-weight: 400;
    letter-spacing: 1px;
    color: var(--ink);
    -webkit-text-stroke: 1.5px var(--outline);
    paint-order: stroke fill;
    text-shadow: 2px 2px 0 var(--outline);
  }
  .credits-panel {
    position: absolute;
    left: 0;
    top: 270px;
    width: 282px;
    height: 296px;
    background: var(--panel);
  }
  .credits {
    position: absolute;
    left: 20px;
    top: 276px;
    width: 258px;
    margin: 0;
    font-family: "Kaushan Script", cursive;
    font-size: 13.5px;
    line-height: 17.6px;
    color: var(--ink);
    text-align: center;
  }
  .credits p { margin: 0; }
  .credits .stay {
    text-align: left;
    padding-left: 14px;
  }
  .credits .social {
    display: flex;
    align-items: center;
    gap: 6px;
    padding-left: 14px;
    text-align: left;
  }
  .social-square {
    width: 10px;
    height: 10px;
    background: var(--ink);
    flex: none;
  }
  .hub {
    position: absolute;
    left: 276px;
    top: 297px;
    width: 270px;
    height: 270px;
    border-radius: 50%;
    background: radial-gradient(circle, var(--page) 0%, var(--page) 60%, var(--hub-ring) 80%, var(--hub-shade) 100%);
    box-shadow: inset 0 0 0 2px rgba(255, 255, 255, 0.9), 0 0 6px rgba(0, 0, 0, 0.15);
  }
  .spindle-hole {
    position: absolute;
    left: 80px;
    top: 80px;
    width: 110px;
    height: 110px;
    border-radius: 50%;
    background: var(--page);
    box-shadow: inset 0 0 0 2px var(--rim);
  }
  .song-title {
    position: absolute;
    left: 0;
    right: 0;
    top: 588px;
    margin: 0;
    text-align: center;
    font-family: "Yesteryear", cursive;
    font-weight: 400;
    font-size: 92px;
    line-height: 1;
    color: var(--ink);
    -webkit-text-stroke: 3px var(--outline);
    paint-order: stroke fill;
    text-shadow: 3px 3px 4px rgba(0, 0, 0, 0.35);
  }
  .song-subtitle {
    position: absolute;
    left: 0;
    right: 0;
    top: 680px;
    margin: 0;
    text-align: center;
    font-family: "Yesteryear", cursive;
    font-size: 48px;
    line-height: 1;
    color: var(--ink);
    -webkit-text-stroke: 2px var(--outline);
    paint-order: stroke fill;
  }
  .subtitle-swash {
    position: absolute;
    left: 190px;
    top: 735px;
    width: 440px;
    height: 40px;
  }
</style>
</head>
<body>
<main class="canvas">
  <section class="disc">
    <div class="disc-artwork" role="img" aria-label="Distressed beach photograph with sky, turquoise sea and sand, overlaid by a dark grainy sketch portrait of the artist wearing sunglasses"></div>

    <h1 class="artist-name">KORVEL</h1>

    <div class="credits-panel"></div>
    <div class="credits">
      <p>Produced by trokay</p>
      <p>Management contact:-</p>
      <p>USA :</p>
      <p>Marla @ +15550148832</p>
      <p>marla@brightwavepr.com</p>
      <p>UK :</p>
      <p>Tamsin @ +447700900417/</p>
      <p>+447700900283</p>
      <p>tamsinbookings@mailhaven.co.uk</p>
      <p>Nigeria :</p>
      <p>Funmi @ +2348000314729</p>
      <p>funmi@korvel-music.com</p>
      <p class="stay">stay connected:</p>
      <p>www.korvel-music.com</p>
      <p class="social"><span class="social-square"></span>chirpline.net/miloskorvel</p>
      <p class="social"><span class="social-square"></span>friendspace.net/miloskorvel</p>
    </div>

    <div class="hub"><div class="spindle-hole"></div></div>

    <h2 class="song-title">Olufunke</h2>
    <p class="song-subtitle">carry me Away</p>
    <svg class="subtitle-swash" viewBox="0 0 440 40" aria-hidden="true">
      <path d="M5 30 C 80 22, 160 18, 250 22 S 380 30, 435 24" fill="none" stroke="#ffffff" stroke-width="6" stroke-linecap="round"/>
      <path d="M5 30 C 80 22, 160 18, 250 22 S 380 30, 435 24" fill="none" stroke="#111111" stroke-width="3" stroke-linecap="round"/>
    </svg>
  </section>
</main>
</body>
</html>
```